Design an Outstanding flyer for my company.

I need a flyer designed for our window tinting company based in Brisbane Queensland Australia. The flyer will be targeting Home tinting. We also do mobile car tinting. Something in regards to this could be incorporated into the flyer as well.
I want it to be 2 sided DL size. Black background.
It really needs to Pop, and be a real attention getter.
It needs to be easy to read.
I have provided a mock up with the info on it from our marketing company. It will need a spellcheck etc to make sure everything is correct.
Everything about it can be changed however you like.
I have also included the company logo.

Lets see what you've got!

Target Market(s)

Home Owners

Industry/Entity Type

Home Improvement

Font styles to use
Other font styles liked:
• Duan Penh

Requirements
Must have
• All the information on the mock up. Clear and easy to read.
• Must Stand Out!

```html
<!DOCTYPE html>
<html lang="en">
<head>
<meta charset="utf-8">
<title>BrightRay Tinting – DL Flyer</title>
<link href="https://fonts.googleapis.com/css2?family=Ubuntu:wght@500;700&display=swap" rel="stylesheet">
<style>
  :root {
    --page: #ffffff;
    --frame: #9a9a9a;
    --flyer-bg: #000000;
    --yellow: #ffe600;
    --gold: #f5a300;
    --white: #ffffff;
    --ink: #111111;
  }
  * { box-sizing: border-box; margin: 0; padding: 0; }
  html, body { width: 1200px; height: 1200px; overflow: hidden; background: var(--page); }
  body { font-family: "Ubuntu", sans-serif; }
  .canvas {
    position: relative; width: 1200px; height: 1200px;
    border: 1px solid var(--frame); background: var(--page);
  }
  .flyer {
    position: absolute; top: 206px; width: 410px; height: 787px;
    background: var(--flyer-bg); overflow: hidden; color: var(--yellow);
  }
  .flyer--front { left: 169px; }
  .flyer--back { left: 621px; }

  .line {
    position: absolute; left: 0; right: 0; text-align: center;
    transform: translateY(-50%); white-space: nowrap; font-weight: 700;
    line-height: 1;
  }
  .headline-heat { font-size: 40px; letter-spacing: 0.5px; }
  .headline-uv { font-size: 27px; }
  .headline-money { font-size: 48px; letter-spacing: 0.5px; }
  .headline-privacy { font-size: 34px; letter-spacing: 0.3px; }
  .reasons { font-size: 22px; }
  .call { font-size: 18px; color: var(--white); }

  .flyer--back .reasons { font-size: 24px; }
  .flyer--back .headline-heat { font-size: 42px; color: var(--white); }
  .flyer--back .headline-uv { font-size: 29px; color: var(--white); }
  .flyer--back .headline-money {
    font-size: 50px;
    background: linear-gradient(180deg, var(--yellow) 0%, var(--gold) 100%);
    -webkit-background-clip: text; background-clip: text; color: transparent;
  }
  .flyer--back .headline-privacy {
    font-size: 34px;
    background: linear-gradient(180deg, var(--yellow) 0%, var(--gold) 100%);
    -webkit-background-clip: text; background-clip: text; color: transparent;
  }

  .rule {
    position: absolute; left: 34px; right: 34px; height: 3px; background: var(--gold);
  }
  .benefits {
    position: absolute; left: 30px; right: 30px;
    font-size: 10px; line-height: 17px; font-weight: 700; color: var(--white);
    text-align: center; text-transform: uppercase;
  }

  .contact-band {
    position: absolute; left: 0; right: 0; top: 602px; height: 70px;
    background: linear-gradient(180deg, #f6b400 0%, var(--yellow) 55%, #fff200 100%);
    color: var(--ink);
  }
  .contact-row {
    position: absolute; left: 82px; font-size: 28px; font-weight: 700;
    line-height: 1; transform: translateY(-50%); white-space: nowrap;
  }
  .contact-row .label { display: inline-block; width: 74px; }
  .contact-row--tel { top: 20px; }
  .contact-row--sms { top: 48px; }

  .brand {
    position: absolute; left: 0; right: 0; top: 710px;
    display: flex; align-items: center; justify-content: center; gap: 10px;
  }
  .brand-dot { width: 22px; height: 22px; border-radius: 50%; background: var(--gold); }
  .brand-name { font-size: 26px; font-weight: 700; color: var(--gold); letter-spacing: 0.5px; }
  .brand-web {
    position: absolute; left: 0; right: 0; top: 748px; text-align: center;
    font-size: 10px; font-weight: 500; color: var(--white);
  }
</style>
</head>
<body>
<main class="canvas">

  <!-- Front side -->
  <section class="flyer flyer--front">
    <div class="line headline-heat" style="top:114px">KEEP HEAT OUT</div>
    <div class="line headline-uv" style="top:154px">BLOCK 99.9% UV RAYS</div>
    <div class="line headline-money" style="top:196px">SAVE MONEY</div>
    <div class="line headline-privacy" style="top:241px">INCREASE PRIVACY</div>

    <div class="rule" style="top:274px"></div>
    <p class="benefits" style="top:281px">
      Reduce glare. Reduce energy costs. Control the amount of light entering your home. Reduce carbon footprint. Make home more beautiful. Eliminate home hot spots. Protect against broken glass. Regulate energy. Protects upholstery. Improve effectiveness of roof insulation. Improve health. Reduces interior floor fading. Eliminate need for blinds. Strengthen your windows. Insulate in winter. Affordable.
    </p>
    <div class="rule" style="top:417px"></div>

    <div class="line reasons" style="top:447px">20 REASONS WHY</div>
    <div class="line reasons" style="top:476px">HOME WINDOW TINTING</div>
    <div class="line reasons" style="top:506px">IS PERFECT FOR YOU.</div>

    <div class="line call" style="top:543px">CALL BRISBANE’S LEADER IN</div>
    <div class="line call" style="top:566px">HOME WINDOW TINTING NOW.</div>

    <div class="contact-band">
      <div class="contact-row contact-row--tel"><span class="label">TEL</span>: 07 3000 1234</div>
      <div class="contact-row contact-row--sms"><span class="label">SMS</span>: 0400 123 456</div>
    </div>

    <div class="brand"><span class="brand-dot"></span><span class="brand-name">BRIGHTRAY TINTING</span></div>
    <div class="brand-web">www.brightraytinting.com.au</div>
  </section>

  <!-- Back side -->
  <section class="flyer flyer--back">
    <div class="line reasons" style="top:78px">20 REASONS WHY</div>
    <div class="line reasons" style="top:112px">HOME WINDOW TINTING</div>
    <div class="line reasons" style="top:146px">IS PERFECT FOR YOU.</div>

    <div class="rule" style="top:178px"></div>

    <div class="line headline-heat" style="top:212px">KEEP HEAT OUT</div>
    <div class="line headline-uv" style="top:258px">BLOCK 99.9% UV RAYS</div>
    <div class="line headline-money" style="top:308px">SAVE MONEY</div>
    <div class="line headline-privacy" style="top:352px">INCREASE PRIVACY</div>

    <p class="benefits" style="top:378px">
      Reduce glare. Reduce energy costs. Control the amount of light entering your home. Reduce carbon footprint. Make home more beautiful. Eliminate home hot spots. Protect against broken glass. Regulate energy. Protects upholstery. Improve effectiveness of roof insulation. Improve health. Reduces interior floor fading. Eliminate need for blinds. Strengthen your windows. Insulate in winter. Affordable.
    </p>
    <div class="rule" style="top:513px"></div>

    <div class="line call" style="top:543px">CALL BRISBANE’S LEADER IN</div>
    <div class="line call" style="top:566px">HOME WINDOW TINTING NOW.</div>

    <div class="contact-band">
      <div class="contact-row contact-row--tel"><span class="label">TEL</span>: 07 3000 1234</div>
      <div class="contact-row contact-row--sms"><span class="label">SMS</span>: 0400 123 456</div>
    </div>

    <div class="brand"><span class="brand-dot"></span><span class="brand-name">BRIGHTRAY TINTING</span></div>
    <div class="brand-web">www.brightraytinting.com.au</div>
  </section>

</main>
</body>
</html>
```